Business Card Design

We need a business card design for a new company located in Missouri City, TX, entitled 'BrightPath Chiropractic & Holistic Center'. Our services include restoration of health and vitality, spinal exam, health assessment, dietary & fitness programs, lymphatic & therapeutic massage, detox & remineralize body wraps, far infrared sauna therapy

Industry/Entity Type

Business

Contact Information for Business Card

BrightPath Chiropractic & Holistic Center, Marlena Oskow LMT, 4512 Hwy. 9, Suite 310, Missouri City, TX 77381, 281-555-0193

```html
<!DOCTYPE html>
<html lang="en">
<head>
<meta charset="utf-8">
<title>BrightPath Chiropractic &amp; Holistic Center – Business Card</title>
<link href="https://fonts.googleapis.com/css2?family=Arimo:wght@400&family=Forum&family=Lusitana:wght@700&display=swap" rel="stylesheet">
<style>
  :root {
    --stage: #ecebe8;
    --teal: #25a38c;
    --teal-light: #2fb89f;
    --blue: #2f6f9e;
    --ink: #0b0b0b;
    --paper: #f7f7f7;
    --grey-type: #6d6e70;
    --white: #ffffff;
  }
  * { box-sizing: border-box; margin: 0; padding: 0; }
  html, body { width: 1200px; height: 902px; overflow: hidden; }
  body {
    background: var(--stage);
    display: flex; flex-direction: column; align-items: center; justify-content: center;
    gap: 40px;
    font-family: "Arimo", Arial, sans-serif;
  }
  .card {
    position: relative; width: 700px; height: 400px; overflow: hidden;
    border-radius: 6px; box-shadow: 0 6px 18px rgba(0,0,0,.18);
  }

  /* Back side */
  .card-back { background: var(--ink); color: var(--white); }
  .card-back .accent { position: absolute; inset: 0; }
  .services { position: absolute; left: 46px; top: 60px; }
  .services-title { color: var(--blue); font-size: 34px; font-weight: 400; margin-bottom: 10px; }
  .services-list { list-style: none; }
  .services-list li {
    font-size: 22px; line-height: 38px; display: flex; align-items: center; gap: 18px;
  }
  .services-list li::before {
    content: ""; width: 11px; height: 11px; border-radius: 50%; background: var(--teal-light); flex: none;
  }

  /* Front side */
  .card-front { background: var(--teal); }
  .card-front .shape { position: absolute; inset: 0; }
  .brand {
    position: absolute; left: 150px; top: 70px; text-align: center;
    font-family: "Lusitana", Georgia, serif; font-weight: 700; color: var(--grey-type);
  }
  .brand-name { font-size: 54px; line-height: 1; }
  .brand-sub { font-size: 21px; margin-top: 6px; }
  .holder { position: absolute; left: 34px; top: 270px; color: var(--white); }
  .holder-name { font-family: "Forum", Georgia, serif; font-size: 42px; line-height: 1; }
  .holder-role { font-size: 22px; margin-top: 4px; }
  .address {
    position: absolute; left: 34px; bottom: 20px; color: var(--white); font-size: 16px;
  }
  .contact {
    position: absolute; left: 430px; top: 250px; color: var(--white); font-size: 16px;
    border-left: 2px solid var(--white); padding-left: 14px; list-style: none;
  }
  .contact li { display: flex; align-items: center; gap: 12px; line-height: 30px; white-space: nowrap; }
  .contact svg { width: 18px; height: 18px; flex: none; }
</style>
</head>
<body>

  <section class="card card-back" aria-label="Card back – services">
    <svg class="accent" viewBox="0 0 700 400" aria-hidden="true">
      <circle cx="620" cy="40" r="130" fill="var(--blue)"/>
      <circle cx="700" cy="170" r="90" fill="var(--teal)"/>
    </svg>
    <div class="services">
      <h2 class="services-title">Services :</h2>
      <ul class="services-list">
        <li>Restoration of health and vitality</li>
        <li>Spinal exam</li>
        <li>Health assessment</li>
        <li>Dietary &amp; fitness programs</li>
        <li>Lymphatic &amp; therapeutic massage</li>
        <li>Detox &amp; remineralize body wraps</li>
        <li>Far infrared sauna therapy</li>
      </ul>
    </div>
  </section>

  <section class="card card-front" aria-label="Card front – contact">
    <svg class="shape" viewBox="0 0 700 400" aria-hidden="true">
      <path d="M0 0 H640 C600 170 420 265 230 262 C140 260 60 240 0 215 Z" fill="var(--paper)"/>
      <path d="M10 222 C80 252 160 272 240 272 C430 272 590 170 650 30 C600 160 440 258 240 260 C160 260 80 245 10 222 Z" fill="var(--ink)"/>
    </svg>
    <div class="brand">
      <div class="brand-name">BrightPath</div>
      <div class="brand-sub">Chiropractic &amp; Holistic Center</div>
    </div>
    <div class="holder">
      <div class="holder-name">Priya Santoro</div>
      <div class="holder-role">Director</div>
    </div>
    <ul class="contact">
      <li>
        <svg viewBox="0 0 24 24"><path fill="var(--white)" d="M6.6 10.8a15 15 0 006.6 6.6l2.2-2.2c.3-.3.7-.4 1-.2 1.1.4 2.3.6 3.6.6.6 0 1 .4 1 1V20c0 .6-.4 1-1 1A17 17 0 013 4c0-.6.4-1 1-1h3.5c.6 0 1 .4 1 1 0 1.3.2 2.5.6 3.6.1.3 0 .7-.2 1z"/></svg>
        281-555-0193
      </li>
      <li>
        <svg viewBox="0 0 24 24"><circle cx="12" cy="12" r="9" fill="none" stroke="var(--white)" stroke-width="2"/><path d="M3 12h18M12 3c3 3 3 15 0 18M12 3c-3 3-3 15 0 18" fill="none" stroke="var(--white)" stroke-width="1.5"/></svg>
        www.brightpath.com
      </li>
      <li>
        <svg viewBox="0 0 24 24"><rect x="3" y="6" width="18" height="12" fill="none" stroke="var(--white)" stroke-width="2"/><path d="M3 6l9 7 9-7" fill="none" stroke="var(--white)" stroke-width="2"/></svg>
        psantoro@brightpath.com
      </li>
    </ul>
    <p class="address">Marlena Oskow LMT, 4512 Hwy. 9, Suite 310, Missouri City, TX 77381</p>
  </section>

</body>
</html>
```